Advertising brochure for Trail Along Southside

We need a new single sided DL flier for the 2020 season!<br/>This flier is for our tour business. You can find all the details about the tour at our web site http://trailalong.southside.example<br/>The flier needs to grab the tourists attention, explain the tour and give price. I will upload a copy of last year's flier for your reference.<br/>We'd like the flier to match our web site to some extent.<br/>The most up to date information is on the web site and NOT last year's brochure. Use the web site for tour itinerary. We NO LONGER do the "Orchard Walk".<br/>Remember the size is "DL". Please no A4 format etc.<br/>You will be able to source images from:<br/>- Our web site<br/>- Our Chatterbook<br/>- Roamreview<br/>- Quarrel Listings<br/>If you have a particular idea in mind then feel free to contact us and we will try to accommodate your photo request.<br/>Good luck!

Target Market(s)

All ages

Industry/Entity Type

Tourism

Requirements
Must have
• Phone number
• Web Site
• Email address
• Price
Nice to have
• Description of tour and images

```html
<!DOCTYPE html>
<html lang="en">
<head>
<meta charset="utf-8">
<title>Trail Along Southside – DL Flier</title>
<link rel="stylesheet" href="https://fonts.googleapis.com/css2?family=Poppins:wght@500;700;800&family=Roboto:wght@300;400&display=swap">
<style>
  :root {
    --orange: #e5791f;
    --orange-bright: #ea7d22;
    --cream: #fde4cc;
    --paper: #eeeeee;
    --ink: #0d0d0d;
    --stage: #e6e9ee;
    --white: #ffffff;
  }
  * { box-sizing: border-box; margin: 0; padding: 0; }
  html, body { width: 1200px; height: 1023px; overflow: hidden; }
  body { background: var(--stage); position: relative; font-family: "Roboto", sans-serif; }

  .flier {
    position: absolute; left: 372px; top: 27px;
    width: 456px; height: 969px;
    background: var(--paper);
    box-shadow: 0 18px 40px rgba(0,0,0,.12);
    overflow: hidden;
  }
  .top-strip { position: absolute; left: 201px; top: 0; width: 241px; height: 9px; background: var(--orange); }

  .brand-badge {
    position: absolute; left: 24px; top: 53px; width: 156px; height: 156px;
    border-radius: 50%; background: var(--orange);
    display: flex; align-items: center; justify-content: center; text-align: center;
  }
  .brand-badge span {
    font-family: "Poppins", sans-serif; font-weight: 700; font-size: 17px; line-height: 1.15;
    color: var(--white); text-transform: uppercase; letter-spacing: .5px; width: 110px;
  }

  .hero-photo {
    position: absolute; left: 201px; top: 17px; width: 241px; height: 213px;
    background: linear-gradient(160deg, #8e8377 0%, #b1a596 35%, #c8bdb0 60%, #9b9084 100%);
  }
  .contact { position: absolute; left: 215px; top: 168px; color: var(--white); font-family: "Poppins", sans-serif; }
  .contact .phone { font-weight: 700; font-size: 21px; line-height: 1.1; }
  .contact .line { font-weight: 700; font-size: 9.5px; line-height: 1.6; text-transform: uppercase; letter-spacing: .2px; }

  .price { position: absolute; left: 22px; top: 232px; font-family: "Poppins", sans-serif; }
  .price .amount { font-weight: 800; font-size: 80px; line-height: 1; color: var(--orange); letter-spacing: -2px; }
  .price .per { font-weight: 700; font-size: 26.5px; line-height: 1; color: var(--ink); margin-top: 2px; margin-left: 2px; letter-spacing: -.6px; }

  .intro { position: absolute; left: 24px; width: 162px; font-family: "Poppins", sans-serif; font-weight: 500; font-size: 14px; line-height: 1.15; color: var(--ink); }
  .intro.one { top: 389px; }
  .intro.two { top: 452px; }

  .tagline {
    position: absolute; left: 22px; top: 570px; width: 170px; height: 368px;
    writing-mode: vertical-rl; transform: rotate(180deg);
    font-family: "Poppins", sans-serif; font-weight: 800; font-size: 50px; line-height: 55px;
    color: var(--ink); text-transform: uppercase; letter-spacing: -1px;
  }
  .tagline .dot { color: var(--orange); }

  .itinerary { position: absolute; left: 201px; top: 241px; width: 241px; height: 715px; background: var(--orange-bright); }
  .stop { position: absolute; left: 16px; width: 212px; color: var(--cream); }
  .stop::before {
    content: ""; position: absolute; left: -23px; top: 2px; width: 14px; height: 14px;
    border-radius: 50%; background: var(--orange-bright); border: 2px solid var(--paper);
  }
  .stop h3 { font-family: "Poppins", sans-serif; font-weight: 700; font-size: 14.5px; line-height: 1.1; text-transform: uppercase; }
  .stop p { font-weight: 300; font-size: 12.3px; line-height: 1.22; margin-top: 3px; }
</style>
</head>
<body>
  <article class="flier">
    <div class="top-strip"></div>

    <div class="brand-badge"><span>Trail Along Southside</span></div>

    <div class="hero-photo" role="img" aria-label="Aerial photo of a convoy of four-wheel-drive vehicles on a dusty desert track through the opal fields"></div>
    <div class="contact">
      <div class="phone">08 5550 1427</div>
      <div class="line">hello@trailalong.southside.example</div>
      <div class="line">trailalong.southside.example</div>
    </div>

    <div class="price">
      <div class="amount">$40</div>
      <div class="per">PER PERSON</div>
    </div>

    <p class="intro one">A Unique Tag-along Journey Through Dustwater Flats.</p>
    <p class="intro two">Experienced Guide Takes You Through A "Day In The Life" Of A Dustwater Flats Miner.</p>

    <h1 class="tagline">Trail<span class="dot">.</span><br>Along<span class="dot">.</span><br>Southside<span class="dot">.</span></h1>

    <section class="itinerary">
      <div class="stop" style="top:31px">
        <h3>Underground<br>Home</h3>
        <p>Our guide's family open the doors of their home and give you a guided tour of their dugout. See how a modern family live underground.</p>
      </div>
      <div class="stop" style="top:147px">
        <h3>Safety Gear</h3>
        <p>All safety gear will be provided for you including helmets and UHF radios. Your safety is our number one priority!</p>
      </div>
      <div class="stop" style="top:229px">
        <h3>Opal Mining</h3>
        <p>We'll make our way down an underground mine where we'll show you the different techniques that modern miners use to extract this beautiful stone.</p>
      </div>
      <div class="stop" style="top:344px">
        <h3>Noodling</h3>
        <p>Next we hit the noodling field to try and find our own opal. With our expert guide showing you how to find opal you'll be a pro in no time!</p>
      </div>
      <div class="stop" style="top:442px">
        <h3>Drive Through<br>The Field</h3>
        <p>Making our way into town, via the opal fields, you'll get a front row seat for viewing our magical landscape that has been terraformed with over 100 years of mining. We might even stop at a scenic lookout for photos on our way!</p>
      </div>
      <div class="stop" style="top:603px">
        <h3>Opal Cutting &amp;<br>Polishing</h3>
        <p>We'll finish up our tour with an opal cutting and polishing demonstration and who knows?... It might be your opal we cut and polish!</p>
      </div>
    </section>
  </article>
</body>
</html>
```